Need a Poster Design A3 for our Cricket Competition

We need a poster design for our upcoming T20 cricket competition Coastline Summer Cup (CSC).

it should say like this:

Bellwick Real Estate (logo supplied)
proudly presents

Coastline Summer Cup (logo supplied)

its a T20 cricket competition

starting 1st April 2018
Registrations Closing : 18th March

prizes worth $5000 to be won

for Registration contact: 0401937265 / 0402816394 and our Facebook page address..see last time's poster

and then sponsors
Updates

Hello.. We will be closing the contest earlier by 5 days so we need to get the design by Tuesday 13th Feb .. Thanks

Industry/Entity Type

Real Estate

Colors

Designer to choose colors to be used in the design.

Requirements
Must have
• emphasis on our main sponsor Bellwick Real Estate & our competition logo

```html
<!DOCTYPE html>
<html lang="en">
<head>
<meta charset="utf-8">
<title>Coastline Summer Cup – T20 Cricket Competition Poster</title>
<link rel="stylesheet" href="https://fonts.googleapis.com/css2?family=Oswald:wght@500;700&family=Montserrat:wght@500;700;800&display=swap">
<style>
  :root{
    --navy:#26307f;
    --red:#d8202a;
    --red-dark:#8e1016;
    --ink:#1d1d1f;
    --sky:#cfe6f7;
    --white:#ffffff;
    --grass:#4f8a2c;
    --gold:#f7a21b;
    --page:#e9e9ea;
  }
  html,body{margin:0;width:1200px;height:899px;overflow:hidden;background:var(--page);}
  .poster{
    position:absolute;left:288px;top:14px;width:666px;height:930px;
    transform:scale(0.9355);transform-origin:0 0;
    background:var(--white);overflow:hidden;
    box-shadow:0 6px 20px rgba(0,0,0,.18);
    font-family:"Montserrat",sans-serif;
  }
  .backdrop{
    position:absolute;left:0;top:0;width:666px;height:806px;
    background:linear-gradient(180deg,#e7f3fb 0%,var(--sky) 30%,#d9e4ec 48%,#9fb3c2 58%,#cfd8de 66%,#7ea35a 72%,var(--grass) 86%,#b8ab8e 100%);
  }
  .host{position:absolute;left:0;width:666px;text-align:center;color:var(--navy);}
  .host-mark{top:24px;width:30px;height:30px;left:318px;background:var(--navy);}
  .host-name{top:64px;font-size:26px;font-weight:700;letter-spacing:3px;}
  .host-sub{top:96px;font-size:10px;font-weight:700;letter-spacing:3px;}
  .presents{top:126px;font-size:14px;font-weight:700;color:var(--ink);letter-spacing:.5px;}
  .cup-emblem{position:absolute;left:92px;top:156px;width:236px;height:168px;border-radius:6px;background:linear-gradient(135deg,rgba(216,32,42,.35),rgba(216,32,42,.08));}
  .cup-initials{position:absolute;left:330px;top:150px;font-family:"Oswald",sans-serif;font-weight:700;font-size:172px;line-height:1;color:var(--navy);letter-spacing:1px;}
  .cup-name{position:absolute;left:0;width:666px;top:326px;text-align:center;font-family:"Oswald",sans-serif;font-weight:700;font-size:40px;color:var(--navy);letter-spacing:3px;text-transform:uppercase;}
  .ribbon{position:absolute;left:60px;top:380px;}
  .ribbon-text{position:absolute;left:60px;top:384px;width:545px;text-align:center;font-weight:800;font-size:25px;color:var(--white);letter-spacing:.5px;line-height:46px;}
  .dates{position:absolute;left:26px;top:512px;font-family:"Oswald",sans-serif;}
  .dates .label{color:var(--red);font-size:20px;font-weight:500;margin:0;line-height:26px;}
  .dates .value{color:var(--ink);font-size:38px;font-weight:500;margin:0 0 6px;line-height:46px;}
  .dates sup{font-size:18px;}
  .prize{position:absolute;left:453px;top:509px;width:184px;height:184px;border-radius:50%;background:radial-gradient(circle at 40% 35%,#ee3035,#b7151c);text-align:center;font-family:"Oswald",sans-serif;box-shadow:0 4px 10px rgba(0,0,0,.25);}
  .prize .line{display:block;color:var(--white);font-size:25px;font-weight:500;line-height:28px;}
  .prize .line.first{margin-top:40px;}
  .prize .amount{display:block;color:var(--gold);font-family:"Montserrat",sans-serif;font-weight:800;font-size:44px;line-height:52px;}
  .contact{position:absolute;left:24px;top:746px;width:614px;height:56px;border:3px solid var(--red);border-radius:14px;background:var(--navy);color:var(--white);text-align:center;}
  .contact .phones{margin:6px 0 0;font-size:20px;font-weight:700;}
  .contact .web{margin:3px 0 0;font-size:14px;font-weight:500;}
  .contact .dot{display:inline-block;width:14px;height:14px;border-radius:50%;background:var(--white);vertical-align:-2px;margin-right:6px;}
  .sponsors{position:absolute;left:0;top:812px;width:666px;height:118px;}
  .sponsor{position:absolute;font-family:"Montserrat",sans-serif;font-weight:700;font-size:13px;text-align:center;line-height:1.15;}
  .s-red{color:var(--red);} .s-navy{color:var(--navy);} .s-ink{color:var(--ink);} .s-gold{color:var(--gold);}
</style>
</head>
<body>
<main class="poster">
  <div class="backdrop" role="img" aria-label="Blurred cricket stadium with sky, stands, green outfield and wooden stumps on the pitch"></div>

  <div class="host host-mark" aria-hidden="true"></div>
  <div class="host host-name">BELLWICK</div>
  <div class="host host-sub">REAL ESTATE</div>
  <div class="host presents">PROUDLY PRESENTS</div>

  <div class="cup-emblem" role="img" aria-label="Competition emblem artwork: cricket ball with a batsman playing a shot"></div>
  <div class="cup-initials">CSC</div>
  <div class="cup-name">Coastline Summer Cup</div>

  <svg class="ribbon" width="545" height="60" viewBox="0 0 545 60" aria-hidden="true">
    <polygon points="0,8 40,8 40,52 0,52 14,30" fill="var(--red-dark)"/>
    <polygon points="545,8 505,8 505,52 545,52 531,30" fill="var(--red-dark)"/>
    <rect x="22" y="2" width="501" height="48" fill="var(--red)"/>
  </svg>
  <div class="ribbon-text">ITS A T20 CRICKET COMPETITION</div>

  <section class="dates">
    <p class="label">STARTING</p>
    <p class="value">1<sup>ST</sup> APRIL 2018</p>
    <p class="label">REGISTRATIONS CLOSING :</p>
    <p class="value">18<sup>TH</sup> MARCH 2018</p>
  </section>

  <div class="prize">
    <span class="line first">PRIZES WORTH</span>
    <span class="amount">$5000</span>
    <span class="line">TO BE WON</span>
  </div>

  <section class="contact">
    <p class="phones">For Registration contact: 0401937265 / 0402816394</p>
    <p class="web"><span class="dot"></span>https://www.socialpage.com/Coastline-Summer-Cup</p>
  </section>

  <section class="sponsors">
    <div class="sponsor s-red" style="left:30px;top:14px;width:95px;">Rosa Sweets</div>
    <div class="sponsor s-ink" style="left:140px;top:14px;width:90px;">Tallow Cotton</div>
    <div class="sponsor s-navy" style="left:245px;top:14px;width:75px;">Kestrel Services</div>
    <div class="sponsor s-red" style="left:345px;top:14px;width:100px;">Harbin Roadlines</div>
    <div class="sponsor s-ink" style="left:470px;top:20px;width:150px;font-size:20px;">Vela TV</div>
    <div class="sponsor s-ink" style="left:38px;top:66px;width:70px;">Lumen Dining</div>
    <div class="sponsor s-ink" style="left:140px;top:66px;width:90px;">Arden Family Trust</div>
    <div class="sponsor s-gold" style="left:245px;top:66px;width:80px;">Quay Migration</div>
    <div class="sponsor s-red" style="left:345px;top:66px;width:100px;">Norvik Grocers</div>
    <div class="sponsor s-ink" style="left:470px;top:70px;width:150px;font-size:17px;">Corel Roadways</div>
  </section>
</main>
</body>
</html>
```